Maple Grove Schools | brand new stationery!

We need stationery design with our new logo! Our company updated it's name and image and we like to incorporate the new one on our stationery, business cards and email signature. We are looking for fresh, new ideas!
Industry: Childcare, Elementary and Middle School
Company Name: Maple Grove Schools
Tagline: Bright Futures Start Here
Main colors: Blue, white and a little yellow
Star shape is something new for us! Do you see a way to incorporate it as a design element?

```html
<!DOCTYPE html>
<html lang="en">
<head>
<meta charset="utf-8">
<title>Maple Grove Schools – Stationery</title>
<link rel="stylesheet" href="https://fonts.googleapis.com/css2?family=Poppins:wght@400;600&family=Questrial&display=swap">
<style>
  :root {
    --navy: #061a78;
    --yellow: #f5b80f;
    --ink: #231f20;
    --paper: #ffffff;
    --backdrop: #e4e5e7;
    --star-haze: #e9e9ea;
  }
  * { margin: 0; padding: 0; box-sizing: border-box; }
  html, body { width: 1200px; height: 832px; overflow: hidden; background: var(--backdrop); }
  .canvas { position: relative; width: 1200px; height: 832px; font-family: "Questrial", sans-serif; color: var(--ink); }

  .piece { position: absolute; background: var(--paper); overflow: hidden; }
  .card-front { left: 60px; top: 70px; width: 270px; height: 162px; background: var(--navy); }
  .card-back { left: 355px; top: 70px; width: 271px; height: 162px; }
  .email-signature { left: 61px; top: 279px; width: 564px; height: 143px; }
  .envelope { left: 59px; top: 478px; width: 567px; height: 284px; }
  .letterhead { left: 648px; top: 68px; width: 497px; height: 697px; }

  .star-haze { position: absolute; background: radial-gradient(ellipse at 45% 60%, var(--star-haze) 0%, rgba(233,233,234,0.6) 45%, rgba(233,233,234,0) 75%); }
  .card-front .star-haze { background: radial-gradient(ellipse at 60% 40%, rgba(3,16,90,0.9) 0%, rgba(3,16,90,0) 70%); }

  .brand { position: absolute; transform: translateX(-50%); text-align: center; }
  .brand-dot { display: block; margin: 0 auto; border-radius: 50%; background: var(--navy); }
  .brand-name { font-family: "Poppins", sans-serif; font-weight: 600; color: var(--ink); line-height: 1.05; white-space: nowrap; }
  .card-front .brand-dot { background: var(--yellow); }
  .card-front .brand-name { color: var(--paper); }

  .tagline { position: absolute; left: 0; width: 100%; top: 114px; text-align: center; font-family: "Poppins", sans-serif; font-weight: 600; font-size: 7.4px; letter-spacing: 0.1px; color: var(--yellow); }

  .person-name { position: absolute; font-family: "Poppins", sans-serif; font-weight: 600; color: var(--navy); line-height: 1; white-space: nowrap; }
  .person-role { position: absolute; color: var(--ink); line-height: 1; }

  .contact-list { position: absolute; list-style: none; color: var(--ink); white-space: nowrap; }
  .contact-list li { display: flex; align-items: center; }
  .contact-icon { flex: none; }

  .rule { position: absolute; width: 1.5px; }
  .rule-navy { background: var(--navy); }
  .rule-yellow { background: var(--yellow); }

  .return-address { position: absolute; left: 19px; top: 257px; font-size: 7px; color: var(--ink); }
</style>
</head>
<body>
<div class="canvas">

  <section class="piece card-front" aria-label="Business card front">
    <div class="star-haze" role="img" aria-label="Scattered star pattern" style="left:150px; top:-10px; width:130px; height:80px;"></div>
    <div class="star-haze" role="img" aria-label="Scattered star pattern" style="left:-10px; top:125px; width:100px; height:45px;"></div>
    <div class="brand" style="left:135px; top:38px;">
      <span class="brand-dot" style="width:30px; height:30px; margin-bottom:7px;"></span>
      <div class="brand-name" style="font-size:15px;">Maple Grove<br>Schools</div>
    </div>
    <p class="tagline">BRIGHT FUTURES START HERE</p>
  </section>

  <section class="piece card-back" aria-label="Business card back">
    <div class="star-haze" role="img" aria-label="Scattered star pattern" style="left:105px; top:100px; width:170px; height:70px;"></div>
    <p class="person-name" style="left:19px; top:24px; font-size:12.5px;">LEAH MORTON</p>
    <p class="person-role" style="left:19px; top:37px; font-size:8px;">Manager</p>
    <div class="brand" style="left:204px; top:20px;">
      <span class="brand-dot" style="width:30px; height:30px; margin-bottom:7px;"></span>
      <div class="brand-name" style="font-size:14px;">Maple Grove<br>Schools</div>
    </div>
    <ul class="contact-list" style="left:19px; top:115px; font-size:6.3px; line-height:9.6px;">
      <li><svg class="contact-icon" width="6" height="6" viewBox="0 0 10 10" style="margin-right:2px;"><circle cx="5" cy="5" r="5" fill="#f5b80f"/><path d="M3.2 2.6l1 1-0.5 0.7a3.6 3.6 0 0 0 1.9 1.9l0.7-0.5 1 1-0.8 0.8C4.7 7.300 2.600 5.300 2.400 3.400z" fill="#fff"/></svg>(+61) 198 765 432</li>
      <li><svg class="contact-icon" width="6" height="6" viewBox="0 0 10 10" style="margin-right:2px;"><circle cx="5" cy="5" r="5" fill="#f5b80f"/><rect x="2.6" y="3.3" width="4.8" height="3.4" fill="none" stroke="#fff" stroke-width="0.8"/><path d="M2.6 3.3L5 5.2 7.4 3.3" fill="none" stroke="#fff" stroke-width="0.8"/></svg>hello@maplegroveschools.edu</li>
      <li><svg class="contact-icon" width="6" height="6" viewBox="0 0 10 10" style="margin-right:2px;"><circle cx="5" cy="5" r="5" fill="#f5b80f"/><circle cx="5" cy="5" r="2.6" fill="none" stroke="#fff" stroke-width="0.7"/><path d="M2.4 5h5.2M5 2.4v5.2" stroke="#fff" stroke-width="0.7"/></svg>www.maplegroveschools.edu</li>
    </ul>
  </section>

  <section class="piece email-signature" aria-label="Email signature">
    <div class="star-haze" role="img" aria-label="Scattered star pattern" style="left:315px; top:55px; width:255px; height:95px;"></div>
    <div class="brand" style="left:80px; top:34px;">
      <span class="brand-dot" style="width:36px; height:36px; margin-bottom:9px;"></span>
      <div class="brand-name" style="font-size:17px;">Maple Grove<br>Schools</div>
    </div>
    <span class="rule rule-navy" style="left:150px; top:32px; height:27px;"></span>
    <p class="person-name" style="left:157px; top:30px; font-size:18.5px;">LEAH MORTON</p>
    <p class="person-role" style="left:157px; top:48px; font-size:11.5px;">Manager</p>
    <span class="rule rule-yellow" style="left:150px; top:73px; height:38px;"></span>
    <ul class="contact-list" style="left:157px; top:66px; font-size:11.3px; line-height:16px;">
      <li><svg class="contact-icon" width="10" height="10" viewBox="0 0 10 10" style="margin-right:3px;"><circle cx="5" cy="5" r="5" fill="#f5b80f"/><path d="M3.2 2.6l1 1-0.5 0.7a3.6 3.6 0 0 0 1.9 1.9l0.7-0.5 1 1-0.8 0.8C4.7 7.300 2.600 5.300 2.400 3.400z" fill="#fff"/></svg>(+61) 198 765 432</li>
      <li><svg class="contact-icon" width="10" height="10" viewBox="0 0 10 10" style="margin-right:3px;"><circle cx="5" cy="5" r="5" fill="#f5b80f"/><rect x="2.6" y="3.3" width="4.8" height="3.4" fill="none" stroke="#fff" stroke-width="0.8"/><path d="M2.6 3.3L5 5.2 7.4 3.3" fill="none" stroke="#fff" stroke-width="0.8"/></svg>hello@maplegroveschools.edu</li>
      <li><svg class="contact-icon" width="10" height="10" viewBox="0 0 10 10" style="margin-right:3px;"><circle cx="5" cy="5" r="5" fill="#f5b80f"/><circle cx="5" cy="5" r="2.6" fill="none" stroke="#fff" stroke-width="0.7"/><path d="M2.4 5h5.2M5 2.4v5.2" stroke="#fff" stroke-width="0.7"/></svg>www.maplegroveschools.edu</li>
    </ul>
  </section>

  <section class="piece envelope" aria-label="Envelope">
    <div class="star-haze" role="img" aria-label="Scattered star pattern" style="left:320px; top:185px; width:255px; height:105px;"></div>
    <div class="brand" style="left:71px; top:19px;">
      <span class="brand-dot" style="width:34px; height:34px; margin-bottom:8px;"></span>
      <div class="brand-name" style="font-size:15px;">Maple Grove<br>Schools</div>
    </div>
    <p class="return-address">Your address, your city, box 88900</p>
  </section>

  <section class="piece letterhead" aria-label="Letterhead">
    <div class="star-haze" role="img" aria-label="Scattered star pattern" style="left:200px; top:590px; width:305px; height:110px;"></div>
    <div class="brand" style="left:67px; top:21px;">
      <span class="brand-dot" style="width:30px; height:30px; margin-bottom:7px;"></span>
      <div class="brand-name" style="font-size:13.5px;">Maple Grove<br>Schools</div>
    </div>
    <ul class="contact-list" style="left:24px; top:636px; font-size:9.3px; line-height:13px;">
      <li><svg class="contact-icon" width="7.5" height="7.5" viewBox="0 0 10 10" style="margin-right:2px;"><circle cx="5" cy="5" r="5" fill="#f5b80f"/><path d="M3.2 2.6l1 1-0.5 0.7a3.6 3.6 0 0 0 1.9 1.9l0.7-0.5 1 1-0.8 0.8C4.7 7.300 2.600 5.300 2.400 3.400z" fill="#fff"/></svg>(+61) 198 765 432</li>
      <li><svg class="contact-icon" width="7.5" height="7.5" viewBox="0 0 10 10" style="margin-right:2px;"><circle cx="5" cy="5" r="5" fill="#f5b80f"/><rect x="2.6" y="3.3" width="4.8" height="3.4" fill="none" stroke="#fff" stroke-width="0.8"/><path d="M2.6 3.3L5 5.2 7.4 3.3" fill="none" stroke="#fff" stroke-width="0.8"/></svg>hello@maplegroveschools.edu</li>
      <li><svg class="contact-icon" width="7.5" height="7.5" viewBox="0 0 10 10" style="margin-right:2px;"><circle cx="5" cy="5" r="5" fill="#f5b80f"/><circle cx="5" cy="5" r="2.6" fill="none" stroke="#fff" stroke-width="0.7"/><path d="M2.4 5h5.2M5 2.4v5.2" stroke="#fff" stroke-width="0.7"/></svg>www.maplegroveschools.edu</li>
    </ul>
  </section>

</div>
</body>
</html>
```